New brand for digital company - your chance to get creative

We need to create a brand for our new business 'Lanternfield Digital'. Please read the brief below before progressing as we are looking for some quite specific outputs.

Background

We are positioning ourselves as ‘marketing technologists’ - we're helping businesses engage with their customers in the online space.

Our tactics include branding, marketing, online management, and social media, however we are differentiating ourselves by focusing on overall strategy, not just tactics. Our tagline is ‘Online made simple’.

We have stipulated some parameters for the brand but otherwise want designers to exercise their creativity.

Requirements
Must have
• We want to see an entire concept, not just a logo.

```html
<!DOCTYPE html>
<html lang="en">
<head>
<meta charset="utf-8">
<title>Lanternfield Digital — Stationery</title>
<link rel="stylesheet" href="https://fonts.googleapis.com/css2?family=Questrial&display=swap">
<style>
  :root {
    --orange: #e87d0e;
    --paper: #ffffff;
    --mist: #dbe6e5;
    --backdrop: #ececec;
    --white: #ffffff;
  }
  * { box-sizing: border-box; margin: 0; padding: 0; }
  html, body { width: 1200px; height: 900px; overflow: hidden; }
  body {
    background: var(--backdrop);
    font-family: "Questrial", sans-serif;
    position: relative;
  }
  .sheet { position: absolute; box-shadow: 0 2px 8px rgba(0,0,0,0.08); }

  /* Letterhead */
  .letterhead { left: 60px; top: 60px; width: 360px; height: 510px; background: var(--paper); }
  .letterhead__band { position: absolute; left: 0; right: 0; bottom: 24px; height: 20px; background: var(--orange); }
  .letterhead__head { position: absolute; right: 18px; top: 20px; text-align: right; color: var(--orange); font-size: 8px; line-height: 1.5; }
  .label { display: inline-block; background: var(--orange); color: var(--white); padding: 2px 6px; }
  .letterhead__head .label:first-child { font-size: 13px; margin-bottom: 4px; }
  .letterhead__mark { position: absolute; left: 22px; bottom: 52px; display: flex; align-items: center; gap: 6px; color: var(--orange); font-size: 13px; }
  .dot { display: inline-block; width: 10px; height: 10px; border-radius: 50%; background: currentColor; }

  /* Folder */
  .folder { left: 460px; top: 60px; width: 360px; height: 510px; background: var(--orange); display: flex; flex-direction: column; align-items: center; justify-content: center; gap: 16px; color: var(--white); }
  .folder__circle { width: 54px; height: 54px; border-radius: 50%; border: 5px solid var(--white); }
  .folder__name { font-size: 30px; }

  /* Business cards */
  .card { width: 260px; height: 150px; }
  .card--front { left: 880px; top: 60px; background: var(--orange); color: var(--white); display: flex; align-items: center; justify-content: center; gap: 10px; font-size: 20px; }
  .card--front .dot { width: 14px; height: 14px; }
  .card--back { left: 880px; top: 240px; background: var(--mist); color: var(--orange); font-size: 8px; line-height: 1.6; text-align: right; padding: 14px 16px; }
  .card--back .label:first-child { font-size: 12px; margin-bottom: 10px; }
  .card__name { font-size: 11px; }

  /* Compliment slip */
  .slip { left: 60px; top: 610px; width: 520px; height: 230px; background: var(--mist); }
  .slip__mark { position: absolute; left: 24px; top: 22px; display: flex; align-items: center; gap: 8px; color: var(--orange); font-size: 26px; }
  .slip__mark .dot { width: 14px; height: 14px; }

  /* Envelope */
  .envelope { left: 620px; top: 610px; width: 520px; height: 230px; background: var(--mist); }
  .envelope__flap { position: absolute; left: 0; right: 0; top: 0; height: 70px; background: var(--orange); display: flex; align-items: center; gap: 8px; padding-left: 22px; color: var(--white); font-size: 18px; }
  .envelope__flap .dot { width: 12px; height: 12px; }
</style>
</head>
<body>
  <section class="sheet letterhead">
    <div class="letterhead__head">
      <span class="label">lanternfield digital</span><br>
      12 Orchard Row, Westmere<br>
      Halden Park, HP4 7QD<br>
      <span class="label">+44 01632 960418</span><br>
      www.lanternfielddigital.co
    </div>
    <div class="letterhead__mark"><span class="dot"></span>lanternfield digital</div>
    <div class="letterhead__band"></div>
  </section>

  <section class="sheet folder">
    <span class="folder__circle"></span>
    <span class="folder__name">lanternfield digital</span>
  </section>

  <section class="sheet card card--front">
    <span class="dot"></span>lanternfield digital
  </section>

  <section class="sheet card card--back">
    <span class="label">lanternfield digital</span><br>
    <span class="card__name">Mara Ellison</span><br>
    Creative Director<br>
    <span class="label">+44 01632 960418</span><br>
    mara@lanternfielddigital.co<br>
    www.lanternfielddigital.co
  </section>

  <section class="sheet slip">
    <div class="slip__mark"><span class="dot"></span>lanternfield digital</div>
  </section>

  <section class="sheet envelope">
    <div class="envelope__flap"><span class="dot"></span>lanternfield digital</div>
  </section>
</body>
</html>
```